Fresh pet feed direct from manufacturer to door step. Quality and Freshness un-surpassed in Industr

Need Business Card Design; leading into many other projects, for New Franchised Business Opportunity providing home delivery of fresh dog and cat feed (no emphasis needed for cat) direct from manufacturing facility. (no middle men or distributors) Food is Farm to Factory fresh. Our trademarked tagline is "Quality is our MAIN Ingredient ! "
Updates

Please take note of other contest for Chirplane Cover and Profile Pic's

Target Market(s)

Dog and Cat owners

Industry/Entity Type

Pet

Contact Information for Business Card

Name, address, local phone, national 800 number, website, email address

Other font styles liked:
• follow that from logo

Requirements
Must have
• Our feed is made in Texas with ingredients sourced from local farms. We want to lean heavy on the Made in West Texas , ranch theme but that has a 'black label', 'vantrel', 'premium', 'high-end' look and feel
Nice to have
• maybe have an offer on card? 20% off with promo code "x" etc.. ?? just a thought...

```html
<!DOCTYPE html>
<html lang="en">
<head>
<meta charset="utf-8">
<title>Holt's Premium – Business Card</title>
<link rel="stylesheet" href="https://fonts.googleapis.com/css2?family=Raleway:wght@400;500;700&display=swap">
<style>
  :root {
    --page: #eceeed;
    --charcoal: #2c292a;
    --bronze: #8f5828;
    --gold-mid: #c99a45;
    --gold-light: #e6c65e;
    --gold-bright: #f6e97a;
    --white: #ffffff;
    --text-font: "Raleway", Arial, sans-serif;
  }
  * { margin: 0; padding: 0; box-sizing: border-box; }
  html, body {
    width: 991px; height: 1200px; overflow: hidden;
    background: var(--page);
    font-family: var(--text-font);
  }
  .card {
    position: absolute; left: 92px; width: 807px; height: 497px;
    overflow: hidden;
  }
  .card--front { top: 82px; background: var(--charcoal); }
  .card--back  { top: 645px; background: var(--charcoal); }

  .gold-field {
    position: absolute; top: 0; height: 100%;
    background: linear-gradient(to bottom,
      var(--bronze) 0%, var(--bronze) 14%, var(--gold-mid) 30%,
      var(--gold-light) 42%, var(--gold-bright) 52%, var(--gold-light) 62%,
      var(--gold-mid) 76%, var(--bronze) 90%, var(--bronze) 100%);
  }
  .card--front .gold-field { left: 92px; width: 623px; }
  .card--back .gold-field--left  { left: 0; width: 105px; }
  .card--back .gold-field--right { left: 702px; width: 105px; }
  .card--back .gold-field--right::before {
    content: ""; position: absolute; left: 0; top: 0; width: 12px; height: 100%;
    background: rgba(0,0,0,0.12);
  }

  .brand-oval {
    position: absolute; left: 146px; top: 120px; width: 508px; height: 268px;
    border-radius: 50%;
    background: var(--charcoal);
    border: 3px solid #2a2324;
    box-shadow: 0 0 0 2px #b3883c inset, 0 0 0 6px rgba(60,40,20,0.35);
    display: flex; align-items: center; justify-content: center; gap: 22px;
  }
  .brand-dot {
    width: 70px; height: 70px; border-radius: 50%; background: var(--white);
    flex: none;
  }
  .brand-name {
    color: var(--white); font-weight: 700; text-align: center;
    line-height: 1;
  }
  .brand-name .brand-word { display: block; font-size: 66px; letter-spacing: 2px; }
  .brand-name .brand-sub  { display: block; font-size: 24px; letter-spacing: 3px; margin-top: 8px; }

  .back-brand {
    position: absolute; left: 462px; top: 58px;
    display: flex; align-items: center; gap: 10px;
  }
  .back-brand .brand-dot { width: 30px; height: 30px; }
  .back-brand .brand-word { font-size: 30px; letter-spacing: 1px; }
  .back-brand .brand-sub { font-size: 11px; letter-spacing: 2px; margin-top: 3px; }

  .person { position: absolute; left: 162px; top: 86px; color: var(--white); }
  .person-name { font-size: 31px; font-weight: 700; line-height: 1.2; }
  .person-role { font-size: 28px; font-weight: 400; line-height: 1.3; margin-top: 2px; }

  .contact-list {
    position: absolute; left: 156px; top: 204px; list-style: none; color: var(--white);
  }
  .contact-list li {
    display: flex; align-items: center; height: 42.5px;
    font-size: 26px; font-weight: 400;
  }
  .contact-list svg {
    width: 26px; height: 26px; margin-right: 17px; flex: none;
    fill: none; stroke: var(--white); stroke-width: 1.8;
  }
</style>
</head>
<body>

<section class="card card--front">
  <div class="gold-field"></div>
  <div class="brand-oval">
    <span class="brand-dot"></span>
    <div class="brand-name">
      <span class="brand-word">HOLT'S</span>
      <span class="brand-sub">PREMIUM</span>
    </div>
  </div>
</section>

<section class="card card--back">
  <div class="gold-field gold-field--left"></div>
  <div class="gold-field gold-field--right"></div>

  <div class="back-brand">
    <span class="brand-dot"></span>
    <div class="brand-name">
      <span class="brand-word">HOLT'S</span>
      <span class="brand-sub">PREMIUM</span>
    </div>
  </div>

  <div class="person">
    <p class="person-name">Your Name</p>
    <p class="person-role">Position</p>
  </div>

  <ul class="contact-list">
    <li>
      <svg viewBox="0 0 24 24"><path d="M6 3l3 4-2 2c1 3 4 6 7 7l2-2 4 3-2 3C10 20 4 14 3 6z"/></svg>
      123-456-7890
    </li>
    <li>
      <svg viewBox="0 0 24 24"><rect x="5" y="2" width="14" height="20" rx="2"/><line x1="10" y1="18.5" x2="14" y2="18.5"/></svg>
      123-456-7888
    </li>
    <li>
      <svg viewBox="0 0 24 24"><rect x="2" y="5" width="20" height="14"/><path d="M2 5l10 8 10-8M2 19l7-7M22 19l-7-7"/></svg>
      name@holtspremium.com
    </li>
    <li>
      <svg viewBox="0 0 24 24"><circle cx="12" cy="12" r="10"/><ellipse cx="12" cy="12" rx="4.5" ry="10"/><path d="M2 12h20M4 7h16M4 17h16M12 2v20"/></svg>
      www.holtspremium.com
    </li>
    <li>
      <svg viewBox="0 0 24 24"><path d="M2 11l10-7 10 7"/><rect x="4" y="11" width="16" height="10"/><rect x="10" y="14" width="4" height="7"/></svg>
      address
    </li>
    <li>
      <svg viewBox="0 0 24 24"><rect x="3" y="3" width="18" height="18" rx="3"/></svg>
      chirplane
    </li>
  </ul>
</section>

</body>
</html>
```